Brellow Publishing

I made a website myself www.brellowpublishing.co.uk a few years ago but I need a new design, which I will code. One that I can be proud of, that 's sexy, to win new customers and showcase my publishing skills. This is a publishing website so I want the home page and books page to be fantastic. I have a logo already so will like the same colour scheme or thereabouts. I have current files and features that I would like to add to your creativity and experience.

Target Market(s)

Web Designers, Graphic Designers

Industry/Entity Type

Book Publisher

Number of Pages Required

5+ page

Font styles to use
Sans Serif

Colors
0255a3
ffffff
ec1f27

Requirements
Must have
• Menu and Sub Menu
• Footer
• Buy Page - Shopping Cart
• Upload feature on the submissions page
• video section on home page (how we publish books)
• Ad space section
Nice to have
• social media bar
• Zoom in page

```html
<!DOCTYPE html>
<html lang="en">
<head>
<meta charset="utf-8">
<title>Brellow Publishing – Self-Publishing That Works</title>
<link rel="stylesheet" href="https://fonts.googleapis.com/css2?family=Open+Sans:ital,wght@0,400;0,600;1,400&family=Cardo&family=Arimo:ital,wght@0,400;0,700;1,400&display=swap">
<style>
  :root{
    --brand-blue:#0255a3;
    --deep-blue:#0a4c93;
    --footer-blue:#0b4a8f;
    --footer-bar:#083d78;
    --brand-red:#ec1f27;
    --leaf-green:#8dc63f;
    --ink:#222;
    --soft-bg:#f1f1f1;
    --card-bg:#e9e9e9;
    --white:#ffffff;
  }
  *{box-sizing:border-box;margin:0;padding:0}
  html,body{width:1200px;height:2862px;overflow:hidden}
  body{position:relative;background:var(--soft-bg);font-family:"Open Sans",Arial,sans-serif;color:var(--ink)}

  /* header */
  .site-header{position:absolute;left:0;top:0;width:1200px;height:99px;background:var(--white)}
  .brand{position:absolute;left:222px;top:30px;display:flex;align-items:center;gap:8px;font:600 17px "Open Sans",sans-serif;color:var(--deep-blue)}
  .brand-dot{width:16px;height:16px;border-radius:50%;background:var(--leaf-green)}
  .topbar{position:absolute;top:12px;left:519px;display:flex;align-items:center;font:12px Arimo,Arial,sans-serif;color:#555}
  .topbar .item{display:flex;align-items:center;gap:7px;margin-right:26px}
  .social{position:absolute;left:841px;top:13px;display:flex;gap:14px}
  .social span{width:13px;height:13px;border-radius:50%;background:#9aa3ad}
  .social span:first-child{background:var(--brand-blue)}
  .main-nav{position:absolute;top:66px;left:0;width:1200px;font:600 12.5px "Open Sans",sans-serif}
  .main-nav a{position:absolute;color:#444;text-decoration:none}
  .main-nav a.active{color:var(--deep-blue)}
  .main-nav a.active::after{content:"";position:absolute;left:0;right:0;top:26px;height:2px;background:var(--deep-blue)}

  /* hero */
  .hero{position:absolute;left:0;top:99px;width:1200px;height:567px;background:linear-gradient(100deg,#b9c3cc 0%,#8a9aa8 30%,#6f7d89 55%,#a8a39c 80%,#3b3f48 100%)}
  .hero-title{position:absolute;left:231px;top:145px;font:400 49px "Open Sans",sans-serif;color:var(--white)}
  .hero-sub{position:absolute;left:235px;top:212px;font:400 29px "Open Sans",sans-serif;color:var(--white)}
  .btn-submit{position:absolute;left:286px;top:309px;width:266px;height:54px;border-radius:27px;background:var(--brand-red);border:3px solid #f5b9bb;color:var(--white);font:400 22px "Open Sans",sans-serif;display:flex;align-items:center;justify-content:center}

  /* intro */
  .intro{position:absolute;left:0;top:666px;width:1200px;height:473px;background:var(--soft-bg)}
  .intro h2{position:absolute;top:36px;width:1200px;text-align:center;font:400 31px Cardo,serif;color:#111}
  .intro p{position:absolute;top:96px;left:250px;width:700px;text-align:center;font:16px/23px Arimo,Arial,sans-serif;color:#444}
  .intro p strong{color:#2a2aa0}
  .feature{position:absolute;top:227px;width:144px;text-align:center}
  .feature .ring{width:144px;height:144px;border-radius:50%;border:2px solid #999;display:flex;align-items:center;justify-content:center}
  .feature.is-active .ring{background:var(--leaf-green);border-color:var(--leaf-green)}
  .feature .label{margin-top:20px;font:600 16px "Open Sans",sans-serif;color:#222}
  .feature.is-active .label{color:var(--leaf-green)}

  /* video */
  .video{position:absolute;left:0;top:1139px;width:1200px;height:368px;background:linear-gradient(90deg,#2a5f93 0%,#3a77b0 45%,#2f6ba4 100%)}
  .video-play{position:absolute;left:544px;top:145px}
  .video-caption{position:absolute;top:255px;width:1200px;text-align:center;font:400 30px "Open Sans",sans-serif;color:var(--white)}

  /* steps */
  .steps{position:absolute;left:0;top:1507px;width:1200px;height:630px}
  .steps h2{position:absolute;top:51px;width:1200px;text-align:center;font:400 28px "Open Sans",sans-serif;color:#111}
  .step{position:absolute;width:362px;height:193px;background:var(--card-bg)}
  .step .num{position:absolute;left:-8px;top:-8px;width:46px;height:46px;border-radius:50%;border:2px solid #d6d6d6;background:var(--soft-bg);font:400 22px "Open Sans",sans-serif;color:var(--brand-blue);display:flex;align-items:center;justify-content:center}
  .step h3{margin-top:22px;text-align:center;font:600 23px "Open Sans",sans-serif;color:#555}
  .step p{margin:18px auto 0;width:320px;text-align:center;font:15.5px/21px Arimo,Arial,sans-serif;color:#6a6a6a}

  /* retailers */
  .retailers{position:absolute;left:225px;top:2137px;width:752px;height:72px;display:flex;align-items:center;justify-content:space-between;font:600 22px "Open Sans",sans-serif;color:#333}

  /* testimonials */
  .testimonials{position:absolute;left:0;top:2209px;width:1200px;height:287px;background:linear-gradient(90deg,#fbfbfb 0%,#f5f5f5 60%,#ece9e4 100%)}
  .testimonials h2{position:absolute;top:34px;width:1200px;text-align:center;font:400 22px "Open Sans",sans-serif;color:#111}
  .quote{position:absolute;top:113px;left:330px;width:540px;text-align:center;font:italic 13px/20px Arimo,Arial,sans-serif;color:#666}
  .quote-rule{position:absolute;top:161px;left:263px;width:676px;height:1px;background:#ccc}
  .avatar{position:absolute;left:528px;top:176px;width:50px;height:50px;border-radius:50%;background:#b9a89a}
  .author{position:absolute;left:591px;top:191px;font:400 15px "Open Sans",sans-serif;color:#222}
  .dots{position:absolute;top:250px;left:553px;display:flex;gap:6px}
  .dots span{width:5px;height:5px;border-radius:50%;background:#ccc}
  .dots span.on{background:#555}

  /* footer */
  .site-footer{position:absolute;left:0;top:2496px;width:1200px;height:328px;background:var(--footer-blue);color:var(--white)}
  .footer-brand{position:absolute;left:229px;top:50px;display:flex;align-items:center;gap:8px;font:600 16px "Open Sans",sans-serif;color:#aac4e4}
  .footer-brand .dot{width:14px;height:14px;border-radius:50%;background:#aac4e4}
  .f-info{position:absolute;left:226px;display:flex;gap:12px;font:13.5px/19px Arimo,Arial,sans-serif;color:#e4ecf6}
  .f-info svg{flex:none;margin-top:2px}
  .footer-col-title{position:absolute;top:28px;font:600 16px "Open Sans",sans-serif}
  .quick-links{position:absolute;left:525px;top:70px;list-style:none;font:13px Arimo,Arial,sans-serif}
  .quick-links li{height:32px;display:flex;align-items:center;gap:12px;color:#e4ecf6}
  .quick-links li::before{content:"";width:5px;height:5px;background:#e4ecf6}
  .quick-links li.current{font-weight:700;color:var(--white)}
  .field{position:absolute;left:723px;width:252px;border:1px solid #6b95c6;font:12px Arimo,Arial,sans-serif;color:#d9e4f1;padding:8px 10px}
  .btn-send{position:absolute;left:723px;top:225px;width:94px;height:28px;border:1px solid #fff;font:13px Arimo,Arial,sans-serif;display:flex;align-items:center;justify-content:center}
  .footer-bar{position:absolute;left:0;top:2824px;width:1200px;height:38px;background:var(--footer-bar);font:10px Arimo,Arial,sans-serif;color:#9fb8d6}
  .footer-bar .copy{position:absolute;left:218px;top:14px}
  .footer-bar .links{position:absolute;left:541px;top:14px}
</style>
</head>
<body>

<header class="site-header">
  <div class="brand"><span class="brand-dot"></span>Brellow Publishing</div>
  <div class="topbar">
    <div class="item">
      <svg width="12" height="12" viewBox="0 0 24 24"><path fill="#7bb33a" d="M6.6 10.8a15.1 15.1 0 0 0 6.6 6.6l2.2-2.2c.3-.3.7-.4 1-.2 1.1.4 2.3.6 3.6.6.6 0 1 .4 1 1V20c0 .6-.4 1-1 1A17 17 0 0 1 3 4c0-.6.4-1 1-1h3.5c.6 0 1 .4 1 1 0 1.3.2 2.5.6 3.6.1.3 0 .7-.2 1z"/></svg>
      +1 555 010 2233
    </div>
    <div class="item">
      <svg width="13" height="10" viewBox="0 0 26 20"><rect width="26" height="20" rx="2" fill="#7bb33a"/><path d="M1 2l12 9 12-9" stroke="#fff" stroke-width="2" fill="none"/></svg>
      hello@brellowmail.example
    </div>
  </div>
  <div class="social"><span></span><span></span><span></span><span></span><span></span></div>
  <nav class="main-nav">
    <a class="active" style="left:413px">Home</a>
    <a style="left:483px">Publishing</a>
    <a style="left:576px">Submissions</a>
    <a style="left:679px">Books</a>
    <a style="left:748px">Authors</a>
    <a style="left:828px">Seminars</a>
    <a style="left:916px">Contact Us</a>
  </nav>
</header>

<section class="hero" role="img" aria-label="Photo of a smiling woman working on a laptop at home">
  <h1 class="hero-title">Brellow Publishing</h1>
  <p class="hero-sub">Self-Publishing That Works</p>
  <a class="btn-submit">SUBMIT BOOK</a>
</section>

<section class="intro">
  <h2>Have a story to tell? We can help you publish your book.</h2>
  <p>Welcome to <strong>Brellow Publishing</strong>, we are an independent publishing company located in London/Surrey. We publish Trade (fiction and non-fiction),<br>&amp; Young Adult (YA) in a variety of subjects.</p>

  <div class="feature is-active" style="left:266px">
    <div class="ring">
      <svg width="90" height="70" viewBox="0 0 90 70"><path d="M45 12C35 4 20 4 8 8v52c12-4 27-4 37 4 10-8 25-8 37-4V8C70 4 55 4 45 12z" fill="none" stroke="#fff" stroke-width="5"/><path d="M45 12v52" stroke="#fff" stroke-width="4"/></svg>
    </div>
    <div class="label">Books</div>
  </div>
  <div class="feature" style="left:525px">
    <div class="ring">
      <svg width="70" height="74" viewBox="0 0 70 74"><circle cx="35" cy="20" r="17" fill="#555"/><path d="M4 74c0-20 13-32 31-32s31 12 31 32z" fill="#555"/></svg>
    </div>
    <div class="label">Authors</div>
  </div>
  <div class="feature" style="left:785px">
    <div class="ring">
      <svg width="80" height="70" viewBox="0 0 80 70"><path d="M40 12c-7-6-17-6-25-3v26c8-3 18-3 25 3 7-6 17-6 25-3V9c-8-3-18-3-25 3z" fill="#555"/><path d="M4 50c8-4 18-4 26 0h18c4 0 4 6 0 6H32m-28 8c12-3 28 2 40 0l26-14c4-2 1-8-3-6L52 52" fill="none" stroke="#555" stroke-width="4" stroke-linejoin="round"/></svg>
    </div>
    <div class="label">Submissions</div>
  </div>
</section>

<section class="video" role="img" aria-label="Video still of stacked books on a blue-toned table">
  <svg class="video-play" width="76" height="76" viewBox="0 0 76 76"><circle cx="38" cy="38" r="36" fill="none" stroke="#fff" stroke-width="3" opacity=".85"/><path d="M30 24l22 14-22 14z" fill="none" stroke="#fff" stroke-width="3" stroke-linejoin="round" opacity=".85"/></svg>
  <p class="video-caption">Learn How We Publish Books</p>
</section>

<section class="steps">
  <h2>Publish Your Book in 4 Easy Steps</h2>
  <article class="step" style="left:233px;top:143px">
    <span class="num">1</span>
    <h3>Writing</h3>
    <p>You write a book to the best of your ability And after redrafting several times when you honestly feel that you have done the best you. Possibly can with it, you send it to us</p>
  </article>
  <article class="step" style="left:614px;top:143px">
    <span class="num">2</span>
    <h3>Submission</h3>
    <p>If your book is in our subject matter and you think you have something that could tickle our fancy, send Us your book for review.</p>
  </article>
  <article class="step" style="left:233px;top:369px">
    <span class="num">3</span>
    <h3>Review</h3>
    <p>You send us your book and our editorial team will look over it and decide if we like it and...</p>
  </article>
  <article class="step" style="left:614px;top:369px">
    <span class="num">4</span>
    <h3>Contract</h3>
    <p>You send us your book and our editorial team will look over it and decide if we like it and then we will Decide what.</p>
  </article>
</section>

<div class="retailers">
  <span>Vellorin</span>
  <span>Quobby</span>
  <span>Tarnleaf</span>
  <span>Pellisk</span>
  <span>Fennow &amp; Drake</span>
  <span>Ovrinote</span>
</div>

<section class="testimonials">
  <h2>Testimonials</h2>
  <p class="quote">"You send us your book and our editorial team will look over it and decide if we like it and then we will Decide what."</p>
  <div class="quote-rule"></div>
  <div class="avatar" role="img" aria-label="Portrait photo of the reviewer"></div>
  <p class="author">Mara Lindqvist</p>
  <div class="dots"><span></span><span class="on"></span><span></span><span></span><span></span><span></span><span></span><span></span><span></span></div>
</section>

<footer class="site-footer">
  <div class="footer-brand"><span class="dot"></span>Brellow Publishing</div>
  <div class="f-info" style="top:160px">
    <svg width="14" height="18" viewBox="0 0 14 18"><path d="M7 0a7 7 0 0 0-7 7c0 5 7 11 7 11s7-6 7-11a7 7 0 0 0-7-7z" fill="#fff"/><circle cx="7" cy="7" r="2.5" fill="#0b4a8f"/></svg>
    <span>Lorem Ipsum is simply dummy<br>text of the printing and<br>typesetting 26594</span>
  </div>
  <div class="f-info" style="top:232px">
    <svg width="14" height="11" viewBox="0 0 26 20"><rect width="26" height="20" rx="2" fill="#fff"/><path d="M1 2l12 9 12-9" stroke="#0b4a8f" stroke-width="2" fill="none"/></svg>
    <span>hello@brellowmail.example</span>
  </div>
  <div class="f-info" style="top:265px">
    <svg width="14" height="14" viewBox="0 0 24 24"><path fill="#fff" d="M6.6 10.8a15.1 15.1 0 0 0 6.6 6.6l2.2-2.2c.3-.3.7-.4 1-.2 1.1.4 2.3.6 3.6.6.6 0 1 .4 1 1V20c0 .6-.4 1-1 1A17 17 0 0 1 3 4c0-.6.4-1 1-1h3.5c.6 0 1 .4 1 1 0 1.3.2 2.5.6 3.6.1.3 0 .7-.2 1z"/></svg>
    <span>+1 555 010 2233</span>
  </div>

  <h4 class="footer-col-title" style="left:525px">Quick Link</h4>
  <ul class="quick-links">
    <li class="current">Home</li>
    <li>Publishing</li>
    <li>Submissions</li>
    <li>Books</li>
    <li>Authors</li>
    <li>Seminars</li>
    <li>Contact Us</li>
  </ul>

  <h4 class="footer-col-title" style="left:727px">Contact Us</h4>
  <div class="field" style="top:74px;height:36px">Name</div>
  <div class="field" style="top:120px;height:88px">Write here</div>
  <div class="btn-send">Submite</div>
</footer>

<div class="footer-bar">
  <span class="copy">Copyright © BRELLOW PUBLISHING &nbsp;|&nbsp; 2017 All Rights Reserved</span>
  <span class="links">Submissions | Books | Authors | Production | Seminars | Contact | Ebooks | Packages | Careers</span>
</div>

</body>
</html>
```